Professional Website Design to match new logo for Medical Legal Company

We have rebranded our company and We want a professional but also dynamic web site design for a group of esteemed doctors that provide expert evaluation of an injured worker in a Workers Compensation case.
​
1. Our target market is both the attorneys who select our doctors and any doctors who would wish to join our group.

2. Notes for the Landing Page:
- We prefer a simpler, sleeker more modern look for the landing page.
- We want a simplified landing page with one image, three buttons highlighted in Content document.
- We want the main image to be black and white but it can be splashed with color.
-We think the landing page might be enhanced by add a dark blue or black as a primary color. Of course please feel free to try any color combination you think might work.
- We want "The Meridale Circle" in large letters and "Stewards of a fair and prompt outcome" in small lettering. We don't want icons on the buttons.
- Do not want more than the one picture at top of landing page.
- We do not want any pictures that include faces. Please eliminate or replace. They will not be chosen.
- For the landing page, instead of a second set of photos please experiment with using medical symbols and legal symbols.
​
3. New Company Name: The Meridale Circle
New logo is uploaded bronze and grey/silver will be colors although we are still tweaking the colors for more metallic feel. Want simple not busy.

4. The overall Web page design needs to have some website design effect (e,g image rollover, scrolling effect, hover effect etc).

5. Please follow the attached word document file for the page content of the 4 web pages. Do not mix it up.

Previous company website: www.clinicjuristpanel.example (we wish to convert some of the content from this website to the new brand). Competitor website that we like: www.docboardly.example

Target Market(s)

Professional Elite. Attorneys and Doctors

Industry/Entity Type

Medical Legal

Coding

Coded - Design and coding required

Number of Pages Required

5+ page

Font styles to use
Other font styles liked:
• Helvetica or maybe font that matches logo. We are open

Colors

Designer to choose colors to be used in the design.

Requirements
Must have
• I can't locate on color scale but we want Bronze and Silver/Grey from logo. Additional colors can be added. Various shades of grey
Nice to have
• Black and white photos, simple elegant design
Should not have
• Images with faces of unknown people

```html
<!DOCTYPE html>
<html lang="en">
<head>
<meta charset="utf-8">
<title>The Meridale Circle</title>
<link rel="stylesheet" href="https://fonts.googleapis.com/css2?family=Cinzel:wght@400;500&family=Barlow:wght@300;400;500&family=Montserrat:wght@500;600&display=swap">
<style>
:root{
  --bronze:#b57a4c;
  --bronze-dark:#9c5f36;
  --ink:#3e3d44;
  --grey-text:#55545b;
  --mist:#eeedf0;
  --band:#5d5c66;
  --footer:#5a5963;
  --white:#ffffff;
  --btn-a:#6f6e77;
  --btn-b:#4b4a52;
}
*{margin:0;padding:0;box-sizing:border-box}
html,body{width:1200px;height:3019px;overflow:hidden;background:var(--white)}
body{position:relative;font-family:'Barlow',sans-serif;color:var(--ink)}
.abs{position:absolute}
.serif{font-family:'Cinzel',serif;font-weight:500}
.caps{font-family:'Montserrat',sans-serif;font-weight:600;letter-spacing:.5px;text-transform:uppercase}

.hero{left:0;top:0;width:1200px;height:493px;background:linear-gradient(100deg,#d8cfc6 0%,#ebe7e3 35%,#eeebe8 60%,#dcd6d2 85%,#cfc9c6 100%)}
.brand{font-family:'Barlow',sans-serif;font-weight:500;font-size:30px;letter-spacing:1px;color:#6b6a72}
.brand-dot{width:22px;height:22px;border-radius:50%;background:var(--bronze);display:inline-block;vertical-align:middle;margin-right:10px}
.menu{left:951px;top:25px;font-family:'Montserrat',sans-serif;font-size:14px;font-weight:500;color:#55545b}
.menu-lines{left:1018px;top:26px;width:40px}
.menu-lines i{display:block;height:2px;background:#77767d;margin-bottom:5px}
.hero-title{left:0;width:1200px;text-align:center;font-size:46px;line-height:54px;letter-spacing:1px}
.hero-title .l1{color:#7a7880}
.hero-title .l2{color:var(--bronze)}
.hero-tagline{left:0;width:1200px;text-align:center;font-family:'Montserrat',sans-serif;font-weight:500;font-size:15px;letter-spacing:3px;text-transform:uppercase;color:#6b6a72}

.h2{font-size:35px;line-height:39px;color:var(--grey-text);letter-spacing:1px}
.rule{height:2px;background:var(--bronze)}
.intro{left:140px;width:920px;top:682px;text-align:center;font-size:20px;font-weight:300;line-height:27px;color:var(--grey-text)}

.feat-icon{width:66px;height:66px;border:1.5px solid var(--bronze);border-radius:50%;display:flex;align-items:center;justify-content:center}
.feat-title{font-weight:500;font-size:18px;line-height:25px;color:var(--ink)}
.feat-text{font-size:14px;font-weight:300;line-height:21px;color:#55545b;margin-top:2px}

.btn{height:63px;display:flex;align-items:center;justify-content:center;text-align:center;color:var(--white);font-family:'Montserrat',sans-serif;font-weight:600;font-size:14px;line-height:16px;letter-spacing:.4px;text-transform:uppercase;background:linear-gradient(90deg,var(--btn-a),var(--btn-b));width:310px}
.btn.accent{background:linear-gradient(90deg,#c0885a,var(--bronze-dark))}

.about{left:0;top:1521px;width:1200px;height:518px;background:var(--mist)}
.about-text{left:554px;top:1704px;width:530px;font-size:20px;font-weight:300;line-height:31px;color:var(--grey-text)}

.doc-col{list-style:none;font-size:18.5px;color:var(--ink)}
.doc-col li{height:42px;display:flex;align-items:center}
.doc-col li::before{content:"";width:7px;height:7px;border-right:2px solid var(--bronze);border-top:2px solid var(--bronze);transform:rotate(45deg);margin-right:12px;margin-left:2px}

.newsletter{left:0;top:2484px;width:1200px;height:145px;background:var(--band)}
.footer{left:0;top:2629px;width:1200px;height:390px;background:var(--footer)}
.foot-title{font-family:'Montserrat',sans-serif;font-weight:600;font-size:16px;letter-spacing:1px;color:var(--white)}
.foot-link{font-size:15px;color:#e2e1e6;line-height:31px}
.social{width:26px;height:26px;border:2px solid var(--white);border-radius:50%}
</style>
</head>
<body>

<!-- Hero -->
<div class="abs hero" role="img" aria-label="Black and white photograph of a Lady Justice statue with scales beside a physician holding a stethoscope"></div>
<div class="abs brand" style="left:127px;top:24px"><span class="brand-dot"></span>MERIDALE CIRCLE</div>
<div class="abs menu">MENU</div>
<div class="abs menu-lines"><i></i><i></i><i></i></div>
<h1 class="abs hero-title serif" style="top:211px"><span class="l1">THE MERIDALE</span><br><span class="l2">CIRCLE</span></h1>
<p class="abs hero-tagline" style="top:336px">Stewards of a fair and prompt outcome</p>

<!-- Commitment -->
<h2 class="abs h2 serif" style="left:0;width:1200px;text-align:center;top:575px">COMMITMENT TO THE HIGHEST STANDARD<br>OF MEDICAL REPORTING</h2>
<div class="abs rule" style="left:560px;top:659px;width:80px"></div>
<p class="abs intro">The Meridale Circle strives to uphold the Highest Standard in Medical Reporting.&nbsp; Following is a list to best describe what to expect when you receive QME Report from one of our Stewards:</p>

<!-- Features row 1 -->
<div class="abs feat-icon" style="left:124px;top:834px"><svg width="32" height="32" viewBox="0 0 32 32" fill="none" stroke="#5a5962" stroke-width="1.5"><circle cx="18" cy="12" r="8"/><path d="M18 7v5l3 2M3 24h6l5 3 9-4M3 20h7l5 2"/></svg></div>
<div class="abs" style="left:202px;top:836px;width:200px"><div class="feat-title">Timely</div><div class="feat-text">Unless special circumstances exist, you can expect to receive the report well ahead of DWC imposed deadlines</div></div>

<div class="abs feat-icon" style="left:449px;top:834px"><svg width="32" height="32" viewBox="0 0 32 32" fill="none" stroke="#5a5962" stroke-width="1.5"><path d="M4 9h11l1 2 1-2h11v17H17l-1 2-1-2H4z"/><path d="M7 16h6M7 20h6M19 16h6M19 20h6"/><circle cx="16" cy="6" r="3"/></svg></div>
<div class="abs" style="left:526px;top:836px;width:200px"><div class="feat-title">Clear, Concise and<br>Readable</div><div class="feat-text">So your valuable time is<br>not wasted</div></div>

<div class="abs feat-icon" style="left:763px;top:828px"><svg width="32" height="32" viewBox="0 0 32 32" fill="none" stroke="#5a5962" stroke-width="1.5"><rect x="4" y="4" width="24" height="24" rx="2"/><circle cx="16" cy="12" r="3"/><path d="M11 24c0-4 2-7 5-7s5 3 5 7M7 8h3M22 8h3M7 20h3M22 20h3"/></svg></div>
<div class="abs" style="left:839px;top:828px;width:210px"><div class="feat-title">Comprehensive Analysis</div><div class="feat-text">of all injured body parts focused on the medical, not legal aspects of the case</div></div>

<!-- Features row 2 -->
<div class="abs feat-icon" style="left:124px;top:983px"><svg width="32" height="32" viewBox="0 0 32 32" fill="none" stroke="#5a5962" stroke-width="1.5"><rect x="6" y="5" width="16" height="22" rx="2"/><path d="M11 5V3h6v2M10 12h8M10 16h8M10 20h5"/><path d="M22 14l5 3-5 3"/></svg></div>
<div class="abs" style="left:202px;top:989px;width:210px"><div class="feat-title">Impartial</div><div class="feat-text">all of our reports are reviewed by a 3rd party for Objectivity</div></div>

<div class="abs feat-icon" style="left:449px;top:983px"><svg width="32" height="32" viewBox="0 0 32 32" fill="none" stroke="#5a5962" stroke-width="1.5"><rect x="5" y="4" width="18" height="24" rx="1"/><path d="M9 9h10M9 13h10M9 17h6"/><rect x="17" y="18" width="10" height="9"/><path d="M20 25v-3M23 25v-5"/></svg></div>
<div class="abs" style="left:526px;top:992px;width:210px"><div class="feat-title">High Level Review of Records by the Physician with Commentary</div></div>

<div class="abs feat-icon" style="left:763px;top:977px"><svg width="32" height="32" viewBox="0 0 32 32" fill="none" stroke="#5a5962" stroke-width="1.5"><path d="M16 26S5 19 5 12a5 5 0 0 1 11-2 5 5 0 0 1 11 2c0 7-11 14-11 14z"/><path d="M8 15h5l2-4 3 7 2-3h4"/><circle cx="25" cy="6" r="3"/></svg></div>
<div class="abs" style="left:839px;top:982px;width:210px"><div class="feat-title">Future Medical<br>Care Section</div><div class="feat-text">that is thoughtful and addresses both the short term and long term needs of the applicant</div></div>

<!-- Features row 3 -->
<div class="abs feat-icon" style="left:124px;top:1136px"><svg width="32" height="32" viewBox="0 0 32 32" fill="none" stroke="#5a5962" stroke-width="1.5"><rect x="10" y="6" width="18" height="20" rx="1"/><path d="M14 12h10M14 16h10M19 20v4M17 22h4"/><circle cx="7" cy="18" r="4"/><circle cx="7" cy="18" r="1.5"/></svg></div>
<div class="abs" style="left:202px;top:1137px;width:210px"><div class="feat-title">Detailed and<br>Comprehensive<br>Medical History</div></div>

<div class="abs feat-icon" style="left:449px;top:1136px"><svg width="32" height="32" viewBox="0 0 32 32" fill="none" stroke="#5a5962" stroke-width="1.5"><rect x="5" y="4" width="16" height="22" rx="1"/><path d="M9 9h8M9 13h5M9 17h4"/><circle cx="20" cy="20" r="5"/><path d="M24 24l4 4"/></svg></div>
<div class="abs" style="left:526px;top:1137px;width:200px"><div class="feat-title">No Conclusory Findings</div><div class="feat-text">Thoroughly discussed conclusions for Apportionment, Causation and Impairment that are medical evidence based</div></div>

<div class="abs feat-icon" style="left:763px;top:1130px"><svg width="32" height="32" viewBox="0 0 32 32" fill="none" stroke="#5a5962" stroke-width="1.5"><path d="M4 12h14v10H10l-4 3v-3H4z"/><path d="M8 16h6M8 19h4"/><circle cx="22" cy="9" r="6"/><path d="M20.5 7.5a1.6 1.6 0 1 1 2 1.6v1.5M22.5 12v.5"/></svg></div>
<div class="abs" style="left:839px;top:1137px;width:200px"><div class="feat-title">Answers to all questions stated&nbsp; in the Cover Letter</div></div>

<!-- Buttons -->
<div class="abs btn" style="left:127px;top:1350px">Schedule an exam</div>
<div class="abs btn" style="left:454px;top:1350px">Contact us with questions<br>regarding upcoming exam</div>
<div class="abs btn accent" style="left:777px;top:1350px">Medical records upload</div>

<!-- About -->
<section class="abs about"></section>
<div class="abs" style="left:175px;top:1640px;width:280px;height:280px;border-radius:50%;background:linear-gradient(135deg,#e3d2c4,#d8d7dc)"></div>
<div class="abs caps" style="left:549px;top:1606px;font-size:17px;color:var(--bronze);letter-spacing:1px">Who we are</div>
<h2 class="abs serif" style="left:546px;top:1636px;font-size:47px;color:var(--grey-text);letter-spacing:1px">ABOUT US</h2>
<p class="abs about-text">Lorem ipsum dolor sit amet, consectetur adipiscing elit, sed do eiusmod tempor incididunt ut labore et dolore magna aliqua. Ut enim ad minim veniam, quis nostrud exercitation ullamco laboris nisi ut aliquip ex ea commodo consequat. Duis aute irure dolor in reprehenderit in voluptate velit esse cillum dolore eu fugiat nulla pariatur. Excepteur sint occaecat cupidatat non proident, sunt in culpa qui officia deserunt mollit anim id est laborum.</p>

<!-- Doctor list -->
<h2 class="abs serif" style="left:135px;top:2117px;font-size:36px;color:var(--grey-text);letter-spacing:1px">DOCTOR LIST</h2>
<div class="abs rule" style="left:135px;top:2162px;width:111px"></div>
<ul class="abs doc-col" style="left:140px;top:2192px"><li>Lorem ipsum dolor</li><li>Aonsectetur adipiscing</li><li>Aed do eiusmod tempor</li><li>Lncididunt ut labore</li><li>Et dolore magna aliqua</li></ul>
<ul class="abs doc-col" style="left:471px;top:2197px"><li>Psum dolor sit amet</li><li>Aonsectetur adipiscing</li><li>Aed do eiusmod tempor</li><li>Lncididunt ut labore</li><li>Et dolore magna aliqua</li></ul>
<ul class="abs doc-col" style="left:803px;top:2196px"><li>Apsum dolor sit amet</li><li>Aonsectetur adipiscing</li><li>Aed do eiusmod tempor</li><li>Lncididunt ut labore</li><li>Et dolore magna aliqua</li></ul>

<!-- Newsletter -->
<section class="abs newsletter"></section>
<div class="abs" style="left:121px;top:2531px;width:3px;height:48px;background:var(--bronze)"></div>
<h3 class="abs serif" style="left:137px;top:2530px;font-size:28px;line-height:27px;color:var(--white);letter-spacing:.5px">DOWNLOAD OUR MOST<br>RECENT NEWSLETTER</h3>
<p class="abs" style="left:524px;top:2537px;width:300px;font-size:16px;line-height:25px;color:#ecebef">Lorem ipsum dolor sit amet, consectetur adipiscing elit, sed do eiusmod</p>
<div class="abs btn accent" style="left:888px;top:2534px;width:190px;height:45px;font-size:14px">Download now</div>

<!-- Footer -->
<footer class="abs footer"></footer>
<div class="abs brand" style="left:141px;top:2683px;color:var(--white)"><span class="brand-dot"></span>MERIDALE CIRCLE</div>
<p class="abs" style="left:135px;top:2770px;width:320px;font-size:14.5px;font-weight:300;line-height:23px;color:#e2e1e6">Lorem ipsum dolor sit amet, consectetur adipiscing elit, sed do eiusmod tempor incididunt ut labore et dolore magna aliqua. Quis ipsum suspendisse ultrices gravida. Risus commodo viverra maecenas accumsan lacus ve</p>

<div class="abs foot-title" style="left:512px;top:2707px">SITEMAP</div>
<div class="abs rule" style="left:608px;top:2717px;width:25px"></div>
<div class="abs foot-link" style="left:512px;top:2739px">About Us<br>Physicians<br>Stakeholder<br>Meridale Gives Back</div>
<div class="abs foot-link" style="left:698px;top:2739px">Terms of Use<br>Privacy Policy<br>Faq<br>Contact Us</div>

<div class="abs foot-title" style="left:873px;top:2702px">STAY IN TOUCH</div>
<div class="abs rule" style="left:1028px;top:2712px;width:25px"></div>
<div class="abs social" style="left:876px;top:2743px"></div>
<div class="abs social" style="left:926px;top:2743px"></div>
<div class="abs social" style="left:977px;top:2743px"></div>
<div class="abs social" style="left:1026px;top:2743px"></div>

<div class="abs" style="left:0;top:2939px;width:1200px;height:1px;background:#73727b"></div>
<p class="abs" style="left:0;top:2964px;width:1200px;text-align:center;font-size:14px;color:#e2e1e6">© 2024 <u>Meridale Circle</u>. All Rights Reserved</p>

</body>
</html>
```